Professional modern business card design

A business card for my nutrition business, wanting a professional look, with info clearly visible. Open to using logo colours too.

Would like key info on the front -
logo
my name and qualifications
email
phone number

and just an enlarged logo again / image on the back.

```html
<!DOCTYPE html>
<html lang="en">
<head>
<meta charset="utf-8">
<title>HL Nutrition – Business Card</title>
<link href="https://fonts.googleapis.com/css2?family=Lato:wght@400;700;900&display=swap" rel="stylesheet">
<style>
  :root {
    --navy: #032840;
    --lime: #d6e021;
    --white: #ffffff;
    --paper: #f6f6f6;
    --backdrop: #1d1d1d;
  }
  * { margin: 0; padding: 0; box-sizing: border-box; }
  html, body {
    width: 1200px; height: 1200px; overflow: hidden;
    background: var(--backdrop);
    font-family: "Lato", Arial, sans-serif;
  }
  .card {
    position: absolute;
    left: 250px;
    width: 700px;
    height: 400px;
    border-radius: 20px;
    overflow: hidden;
  }
  .brand-name {
    position: absolute;
    font-weight: 900;
    line-height: 1;
    white-space: nowrap;
  }

  /* Front */
  .card--front { top: 170px; background: var(--navy); }
  .card--front .brand-name {
    right: 47px; top: 86px;
    font-size: 40px;
    color: var(--white);
  }
  .holder { position: absolute; left: 47px; top: 216px; }
  .holder-name {
    color: var(--white); font-weight: 900; font-size: 31px; letter-spacing: 0.2px;
    text-transform: uppercase; line-height: 1;
  }
  .holder-role {
    margin-top: 8px; color: var(--lime); font-size: 18.5px; font-weight: 400; letter-spacing: 0.2px;
  }
  .divider {
    position: absolute; left: 47px; top: 286px; width: 603px; height: 3px; background: var(--white);
  }
  .contacts { position: absolute; left: 47px; top: 304px; list-style: none; }
  .contact { display: flex; align-items: center; color: var(--white); }
  .contact--phone { font-size: 21px; height: 28px; }
  .contact--email { font-size: 18px; height: 26px; margin-top: 1px; }
  .contact-icon { width: 14px; height: 14px; margin-right: 11px; flex: none; }
  .edge-band { position: absolute; left: 0; bottom: 0; width: 700px; height: 16px; }

  /* Back */
  .card--back { top: 631px; background: var(--paper); }
  .back-visual {
    position: absolute; inset: 0;
    background:
      radial-gradient(ellipse at 72% 45%, #e9e9e9 0%, rgba(233,233,233,0) 60%),
      linear-gradient(160deg, #f3f3f3 0%, #ececec 45%, #f8f8f8 100%);
  }
  .card--back .brand-name {
    left: 147px; top: 160px;
    font-size: 72px;
    color: var(--navy);
  }
</style>
</head>
<body>

<section class="card card--front" aria-label="Business card front">
  <p class="brand-name">HL Nutrition</p>

  <div class="holder">
    <h1 class="holder-name">Harriet Lowe</h1>
    <p class="holder-role">Specialist Rehabilitation Dietitian</p>
  </div>

  <div class="divider"></div>

  <ul class="contacts">
    <li class="contact contact--phone">
      <svg class="contact-icon" viewBox="0 0 24 24" aria-hidden="true">
        <path fill="var(--lime)" d="M6.6 10.8c1.4 2.8 3.8 5.1 6.6 6.6l2.2-2.2c.3-.3.7-.4 1-.2 1.1.4 2.3.6 3.6.6.6 0 1 .4 1 1V20c0 .6-.4 1-1 1C10.6 21 3 13.4 3 4c0-.6.4-1 1-1h3.5c.6 0 1 .4 1 1 0 1.3.2 2.5.6 3.6.1.3 0 .7-.2 1L6.6 10.8z"/>
        <path fill="none" stroke="var(--lime)" stroke-width="2" d="M14 3.5a7 7 0 0 1 6.5 6.5M14 7a3.5 3.5 0 0 1 3 3"/>
      </svg>
      07700900418
    </li>
    <li class="contact contact--email">
      <svg class="contact-icon" viewBox="0 0 24 18" aria-hidden="true">
        <rect x="1" y="1" width="22" height="16" fill="var(--lime)"/>
        <path d="M1 1l11 9 11-9" fill="none" stroke="var(--navy)" stroke-width="2"/>
      </svg>
      harriet@hlnutrition.co.uk
    </li>
  </ul>

  <svg class="edge-band" viewBox="0 0 700 16" preserveAspectRatio="none" aria-hidden="true">
    <polygon points="0,0 465,0 451,16 0,16" fill="var(--lime)"/>
    <polygon points="479,0 700,0 700,16 465,16" fill="var(--white)"/>
  </svg>
</section>

<section class="card card--back" aria-label="Business card back">
  <div class="back-visual" role="img" aria-label="Soft faded photograph of a coiled tape measure"></div>
  <p class="brand-name">HL Nutrition</p>
</section>

</body>
</html>
```